Brisk Framing website

I need a website for my construction. I want customers to see past builds and current projects Something that stands out and reflects awareness, safety, attention to details. I already have a logo designed by Pixel Harbor
Target Market(s)
Residential and Commercial sectors
Industry/Entity Type
Construction
Logo Text
Brisk Framing
Colors
EB3D1F
EC4F4E
F09395
F8D3D4
FCEDEE
Requirements
Must have
- My contact info
Nice to have
- Past projects

```html
<!DOCTYPE html>
<html lang="en">
<head>
<meta charset="utf-8">
<title>Brisk Framing</title>
<link href="https://fonts.googleapis.com/css2?family=Montserrat:wght@400;500;600;700;800&family=Orbitron:wght@700;900&display=swap" rel="stylesheet">
<style>
:root{
  --red:#e3261b;
  --red-soft:#ec4f4e;
  --pink:#f09395;
  --blush:#f8d3d4;
  --mist:#fcedee;
  --ink:#1d1d1d;
  --text:#3a3a3a;
  --muted:#6a6a6a;
  --dark:#2b2b2b;
  --white:#ffffff;
}
*{margin:0;padding:0;box-sizing:border-box}
html,body{width:1200px;height:4342px;overflow:hidden}
body{position:relative;background:var(--white);font-family:"Montserrat",sans-serif;color:var(--text)}
.abs{position:absolute}
.display{font-family:"Orbitron",sans-serif;font-weight:900;letter-spacing:2px;color:var(--ink)}
/* header */
.site-header{position:absolute;left:0;top:0;width:1200px;height:105px;background:var(--white);z-index:5}
.logo{position:absolute;left:147px;top:32px;display:flex;align-items:center;gap:10px;font-weight:800;font-size:26px;color:var(--red);letter-spacing:1px}
.logo-mark{width:18px;height:18px;background:var(--red)}
.call-tab{position:absolute;left:660px;top:0;width:348px;height:40px;background:var(--red);clip-path:polygon(0 0,100% 0,94% 100%,6% 100%);color:var(--white);font-weight:700;font-size:17px;display:flex;align-items:center;justify-content:center;gap:10px}
.nav{position:absolute;top:68px;left:490px;display:flex;gap:0;font-weight:700;font-size:14px;color:var(--ink)}
.nav a{position:absolute;white-space:nowrap;text-decoration:none;color:var(--ink)}
.nav a.active{color:var(--red)}
/* hero */
.hero-photo{position:absolute;left:0;top:105px;width:1200px;height:730px;background:linear-gradient(180deg,#2a2a2a 0%,#777 45%,#3a3a3a 100%);clip-path:polygon(0 0,100% 0,100% 67.5%,29.5% 100%,0 67.5%)}
.hero-wedge{position:absolute;left:0;top:0;width:1200px;height:880px}
.hero-title{position:absolute;left:0;width:1200px;text-align:center}
.hero-title.top{top:268px;font-size:72px;color:var(--white)}
.hero-title.bottom{top:356px;font-size:78px;color:var(--red)}
/* sections */
.marker{position:absolute;width:2px;background:var(--red)}
.marker-num{position:absolute;font-family:"Orbitron",sans-serif;font-weight:900;font-style:italic;font-size:16px;color:var(--red)}
.section-title{position:absolute;font-size:44px}
.about-text{position:absolute;left:147px;top:1100px;width:380px;font-size:14px;line-height:26.5px;text-align:justify;color:var(--text)}
.btn{position:absolute;display:flex;align-items:center;justify-content:center;font-weight:700;font-size:14px;background:var(--red);color:var(--white)}
.btn.ghost{background:var(--white);color:var(--red);border:2px solid var(--red)}
.photo{position:absolute}
.blueprint{position:absolute;background:linear-gradient(180deg,#f4f4f4,#fafafa);}
.grid-tile{position:absolute}
.zoom{position:absolute;left:572px;top:2142px;width:56px;height:56px;border-radius:50%;background:var(--white);display:flex;align-items:center;justify-content:center}
/* team */
.member{position:absolute;top:2890px;width:260px;text-align:center}
.member .ring{width:236px;height:236px;margin:0 auto;border-radius:50%;border:2px solid var(--pink);background:var(--white);display:flex;align-items:center;justify-content:center;position:relative}
.member .portrait{width:186px;height:186px;border-radius:50%;background:linear-gradient(160deg,#9aa4ae,#3b4550)}
.member .badge{position:absolute;left:96px;bottom:-20px;width:44px;height:44px;border-radius:50%;background:var(--red)}
.member h3{margin-top:34px;font-size:19px;font-weight:700;color:var(--ink);letter-spacing:.5px}
.member p{margin-top:8px;font-size:13px;line-height:22px;color:var(--muted)}
.arrow{position:absolute;top:2975px}
/* contact */
.contact-info{position:absolute;left:652px;top:3428px;color:var(--white)}
.contact-info h4{font-size:24px;font-weight:600;color:var(--white);letter-spacing:.5px}
.contact-info .line{display:flex;gap:12px;margin-top:22px;font-size:14px;line-height:22px}
.contact-info .call{display:flex;gap:12px;align-items:center;margin-top:16px;font-size:17px;font-weight:700}
.field{position:absolute;border-bottom:1px solid #777;color:var(--white);font-size:13px;padding-bottom:16px}
.footer{position:absolute;left:0;top:4241px;width:1200px;height:101px;background:var(--white)}
.footer p{position:absolute;left:143px;top:44px;font-size:12.5px;color:var(--muted)}
.social{position:absolute;top:46px;width:16px;height:16px;border-radius:50%}
</style>
</head>
<body>

<header class="site-header">
  <div class="logo"><span class="logo-mark"></span>Brisk Framing</div>
  <div class="call-tab">
    <svg width="18" height="18" viewBox="0 0 24 24"><path fill="#fff" d="M6.6 10.8a15.1 15.1 0 0 0 6.6 6.6l2.2-2.2c.3-.3.7-.4 1-.2 1.1.4 2.3.6 3.6.6.6 0 1 .4 1 1V20c0 .6-.4 1-1 1A17 17 0 0 1 3 4c0-.6.4-1 1-1h3.5c.6 0 1 .4 1 1 0 1.3.2 2.5.6 3.6.1.3 0 .7-.2 1z"/></svg>
    CALL US : +1 555 014 2290
  </div>
  <nav class="nav">
    <a class="active" href="#" style="left:12px">HOME</a>
    <a href="#" style="left:88px">ABOUT</a>
    <a href="#" style="left:170px">SERVICES</a>
    <a href="#" style="left:272px">PROJECTS</a>
    <a href="#" style="left:377px">TEAM</a>
    <a href="#" style="left:450px">CONTACT</a>
  </nav>
  <svg class="abs" style="left:485px;top:66px" width="60" height="28" viewBox="0 0 60 28"><path d="M2 2h56L30 26z" fill="none" stroke="#e3261b" stroke-width="2"/></svg>
  <svg class="abs" style="left:1038px;top:68px" width="18" height="18" viewBox="0 0 24 24"><circle cx="10" cy="10" r="7" fill="none" stroke="#e3261b" stroke-width="3"/><path d="M15 15l7 7" stroke="#e3261b" stroke-width="3"/></svg>
</header>

<!-- hero -->
<svg class="hero-wedge" viewBox="0 0 1200 880"><polygon points="0,598 354,880 1200,598 1200,560 354,838 0,560" fill="#e3261b"/></svg>
<div class="hero-photo" role="img" aria-label="Black and white city construction site with tower cranes at dusk"></div>
<h1 class="hero-title top display">BRISK</h1>
<h2 class="hero-title bottom display">FRAMING</h2>
<svg class="abs" style="left:533px;top:499px" width="100" height="100" viewBox="0 0 100 100"><circle cx="50" cy="50" r="45" fill="none" stroke="#fff" stroke-width="6"/><path d="M40 30v40l32-20z" fill="#fff"/></svg>

<!-- about -->
<div class="marker" style="left:353px;top:880px;height:95px"></div>
<div class="marker-num" style="left:367px;top:964px">01</div>
<h2 class="section-title display" style="left:147px;top:1022px">ABOUT</h2>
<p class="about-text">Lorem ipsum dolor sit amet, consectetur adipiscing elit, sed do eiusmod tempor incididunt ut labore et dolore magna aliquis ipsum suspendi viverraecenas accumsan lacus vel facium dolor sit amet, consectetur adipiscing elit, sed do eiusmod tempor incididunt ut labore et dolore magna aliquis ipsum suspendismmodo viverra maecenas accumsan lacus vel facilisisorem ipsum dolor sit amet, consectetur adipiscing elit,</p>
<div class="btn" style="left:147px;top:1350px;width:150px;height:47px">READ MORE</div>
<div class="photo" style="left:600px;top:854px;width:455px;height:528px;background:linear-gradient(180deg,#a9c8e6,#dfe7ee 60%,#c9ccd0)" role="img" aria-label="Two engineers in white hard hats reviewing plans on site"></div>
<svg class="abs" style="left:581px;top:1328px" width="494" height="87" viewBox="0 0 494 87"><polygon points="0,87 245,0 494,87" fill="#e3261b"/></svg>

<!-- projects -->
<div class="blueprint" style="left:0;top:1420px;width:1200px;height:435px" role="img" aria-label="Faint architectural drawing with a building cutaway"></div>
<div class="marker" style="left:609px;top:1483px;height:100px"></div>
<div class="marker-num" style="left:638px;top:1572px">02</div>
<h2 class="section-title display" style="left:0;width:1200px;text-align:center;top:1628px">PROJECTS</h2>
<div class="btn" style="left:384px;top:1729px;width:191px;height:45px">PAST PROJECTS</div>
<svg class="abs" style="left:463px;top:1774px" width="32" height="16" viewBox="0 0 32 16"><path d="M0 0h32L16 16z" fill="#e3261b"/></svg>
<div class="btn ghost" style="left:591px;top:1729px;width:225px;height:45px">CURRENT PROJECTS</div>

<div class="grid-tile" style="left:8px;top:1855px;width:390px;height:312px;background:linear-gradient(180deg,#4a86c4,#b59a62)" role="img" aria-label="Concrete towers rising beside a yellow crane"></div>
<div class="grid-tile" style="left:8px;top:2175px;width:390px;height:314px;background:linear-gradient(180deg,#8a7a66,#5a6e3a)" role="img" aria-label="Two site workers in hard hats checking a tablet"></div>
<div class="grid-tile" style="left:406px;top:1855px;width:388px;height:634px;background:linear-gradient(180deg,#b51d12,#7a0f0a)" role="img" aria-label="Worker on rebar columns under a red sky"></div>
<div class="zoom"><svg width="20" height="20" viewBox="0 0 24 24"><circle cx="10" cy="10" r="6" fill="none" stroke="#e3261b" stroke-width="3"/><path d="M14.5 14.5l6 6" stroke="#e3261b" stroke-width="3"/></svg></div>
<div class="grid-tile" style="left:802px;top:1855px;width:389px;height:312px;background:linear-gradient(180deg,#7d8fb0,#d7a46b 60%,#9a8a7a)" role="img" aria-label="House frame with steel roof trusses at sunset"></div>
<div class="grid-tile" style="left:802px;top:2175px;width:389px;height:314px;background:linear-gradient(180deg,#3c74b8,#8f8a78)" role="img" aria-label="Multi-storey concrete frame with a crane"></div>
<div class="btn" style="left:524px;top:2538px;width:152px;height:45px">LOAD MORE</div>

<!-- team -->
<div class="blueprint" style="left:0;top:2600px;width:1200px;height:700px;background:linear-gradient(180deg,#f6f6f6,#ffffff)" role="img" aria-label="Faint architectural drawing backdrop"></div>
<div class="marker" style="left:609px;top:2629px;height:92px"></div>
<div class="marker-num" style="left:638px;top:2710px">03</div>
<h2 class="section-title display" style="left:0;width:1200px;text-align:center;top:2768px">OUR TEAM</h2>
<svg class="arrow" style="left:68px" width="34" height="66" viewBox="0 0 34 66"><path d="M32 2L2 33l30 31" fill="none" stroke="#bbb" stroke-width="2"/></svg>
<svg class="arrow" style="left:1098px" width="34" height="66" viewBox="0 0 34 66"><path d="M2 2l30 31L2 64" fill="none" stroke="#bbb" stroke-width="2"/></svg>
<div class="member" style="left:135px"><div class="ring"><div class="portrait" role="img" aria-label="Team member portrait"></div><span class="badge"></span></div><h3>MARCO VELL</h3><p>Sed ut perspiciatis unmnis<br>iste natus</p></div>
<div class="member" style="left:472px"><div class="ring"><div class="portrait" role="img" aria-label="Team member portrait" style="background:linear-gradient(160deg,#e8dccb,#8a7a6a)"></div><span class="badge"></span></div><h3>LENA OSTROW</h3><p>Sed ut perspiciatis unmnis<br>iste natus</p></div>
<div class="member" style="left:805px"><div class="ring"><div class="portrait" role="img" aria-label="Team member portrait" style="background:linear-gradient(160deg,#c9d6e2,#2d3846)"></div><span class="badge"></span></div><h3>THEO BRANIK</h3><p>Sed ut perspiciatis unmnis<br>iste natus</p></div>

<!-- contact -->
<svg class="abs" style="left:0;top:3317px" width="1200" height="924" viewBox="0 3317 1200 924">
  <polygon points="0,3606 846,3317 1200,3606" fill="#e3261b"/>
  <polygon points="0,3606 480,3471 785,3707 1053,3505 1200,3606 1200,4241 0,4241" fill="#2b2b2b"/>
  <polygon points="480,3471 785,3707 1053,3505 1040,3497 785,3690 490,3465" fill="#e3261b"/>
</svg>
<div class="abs" style="left:0;top:3900px;width:1200px;height:341px;background:linear-gradient(180deg,rgba(43,43,43,0),#0f0f0f)" role="img" aria-label="Silhouettes of workers and scaffolding across a city skyline"></div>
<div class="contact-info">
  <h4>CONTACT INFO</h4>
  <div class="line"><svg width="14" height="18" viewBox="0 0 14 18"><path d="M7 0a7 7 0 0 0-7 7c0 5 7 11 7 11s7-6 7-11a7 7 0 0 0-7-7zm0 10a3 3 0 1 1 0-6 3 3 0 0 1 0 6z" fill="#fff"/></svg><span>123,Sed ut perspiciatis unde omnis isatus<br>error sluptatem accusantium</span></div>
  <div class="call"><svg width="18" height="18" viewBox="0 0 24 24"><path fill="#fff" d="M6.6 10.8a15.1 15.1 0 0 0 6.6 6.6l2.2-2.2c.3-.3.7-.4 1-.2 1.1.4 2.3.6 3.6.6.6 0 1 .4 1 1V20c0 .6-.4 1-1 1A17 17 0 0 1 3 4c0-.6.4-1 1-1h3.5c.6 0 1 .4 1 1 0 1.3.2 2.5.6 3.6.1.3 0 .7-.2 1z"/></svg>CALL US : +1 555 014 2290</div>
</div>
<div class="marker" style="left:169px;top:3606px;height:52px"></div>
<div class="marker-num" style="left:197px;top:3641px">04</div>
<h2 class="section-title display" style="left:145px;top:3680px;color:#fff">CONTACT</h2>
<div class="field" style="left:143px;top:3784px;width:408px">Enter Name</div>
<div class="field" style="left:598px;top:3784px;width:406px">Enter Email</div>
<div class="field" style="left:143px;top:3880px;width:408px">Enter Phone</div>
<div class="field" style="left:598px;top:3880px;width:406px">Address</div>
<div class="field" style="left:143px;top:3978px;width:861px;padding-bottom:76px">Message</div>
<div class="btn" style="left:145px;top:4124px;width:152px;height:47px">SUBMIT</div>

<footer class="footer">
  <p>© 2022 Copyright Brisk Framing . All Rights Reserved &nbsp;|&nbsp; Terms and Conditions</p>
  <span class="social" style="left:986px;background:var(--dark)"></span>
  <span class="social" style="left:1010px;background:var(--red)"></span>
  <span class="social" style="left:1034px;background:var(--dark)"></span>
</footer>

</body>
</html>
```